Email Design Creative Design Needed

Our website is called CampusLedger.org. One of our competitor(varsity scout.us.com) is using the following email creative.
http://pqr.brightquill.com/Affiliate/Assets/3532.html
http://pqr.brightquill.com/Affiliate/Assets/7921.html
http://pqr.brightquill.com/Affiliate/Assets/8061.html

We would like to use similar email creative without copying their exact creative. You can use the above as a guide but then come up with your own version of the creative.
The above are just concepts, please be creative and come up with your own version of it, without feeling that they have been copied. Feel free to move the components around. Also, feel free to change the colours and text.

Please find attached the CampusLedger.org logo.

Reason: We would like to receive more designs.

College

```html
<!DOCTYPE html>
<html lang="en">
<head>
<meta charset="utf-8">
<title>CampusLedger.org – Explore Degrees by Subject</title>
<link rel="stylesheet" href="https://fonts.googleapis.com/css2?family=Source+Sans+3:wght@400;600;700&display=swap">
<style>
  :root {
    --paper: #ffffff;
    --navy: #1d3557;
    --navy-deep: #14263f;
    --accent: #f4a261;
    --brand-mark: #2a9d8f;
    --card: #ffffff;
    --card-text: #1d3557;
    --muted: #4a5568;
    --footer-text: #dbe4f0;
  }
  * { box-sizing: border-box; margin: 0; padding: 0; }
  html, body {
    width: 1200px;
    height: 1000px;
    overflow: hidden;
    background: var(--paper);
    font-family: "Source Sans 3", Arial, sans-serif;
  }
  .email {
    width: 1200px;
    height: 1000px;
    display: flex;
    flex-direction: column;
  }
  .masthead {
    height: 200px;
    background: var(--paper);
    display: flex;
    flex-direction: column;
    align-items: center;
    justify-content: center;
    gap: 18px;
    border-bottom: 8px solid var(--accent);
  }
  .brand {
    display: flex;
    align-items: center;
    gap: 16px;
  }
  .brand-square {
    width: 44px;
    height: 44px;
    border-radius: 8px;
    background: var(--brand-mark);
  }
  .brand-name {
    font-size: 52px;
    font-weight: 700;
    line-height: 1;
    color: var(--navy);
  }
  .tagline {
    font-size: 24px;
    line-height: 1.2;
    color: var(--muted);
  }
  .subject-band {
    flex: 1;
    background: var(--navy);
    padding: 40px 36px 0;
    display: flex;
    flex-direction: column;
  }
  .band-heading {
    font-size: 26px;
    font-weight: 600;
    color: var(--accent);
    text-align: center;
    letter-spacing: 1px;
    text-transform: uppercase;
    margin-bottom: 28px;
  }
  .subject-grid {
    display: grid;
    grid-template-columns: repeat(3, 360px);
    grid-auto-rows: 68px;
    gap: 16px 24px;
    justify-content: center;
  }
  .subject-tile {
    display: flex;
    align-items: center;
    justify-content: space-between;
    padding: 0 24px;
    background: var(--card);
    color: var(--card-text);
    border-left: 8px solid var(--accent);
    border-radius: 6px;
    font-size: 24px;
    font-weight: 600;
    text-decoration: none;
    white-space: nowrap;
  }
  .subject-tile svg { flex: none; }
  .subject-tile.last-left { grid-column: 1 / 2; margin-left: 192px; margin-right: -192px; }
  .subject-tile.last-right { grid-column: 2 / 3; margin-left: 192px; margin-right: -192px; }
  .footer-links {
    margin-top: auto;
    background: var(--navy-deep);
    margin-left: -36px;
    margin-right: -36px;
    padding: 22px 40px;
    display: flex;
    flex-wrap: wrap;
    justify-content: center;
    gap: 8px 22px;
    font-size: 20px;
    line-height: 24px;
  }
  .footer-links a {
    color: var(--footer-text);
    text-decoration: none;
    white-space: nowrap;
  }
</style>
</head>
<body>
<div class="email">
  <header class="masthead">
    <div class="brand">
      <span class="brand-square"></span>
      <span class="brand-name">CampusLedger.org</span>
    </div>
    <p class="tagline">Pick a subject, compare programs and take the next step toward a new career.</p>
  </header>

  <section class="subject-band">
    <h2 class="band-heading">Explore degrees by subject</h2>
    <div class="subject-grid">
      <a class="subject-tile" href="#">Art &amp; Design<svg width="14" height="22" viewBox="0 0 14 22"><path d="M3 3l8 8-8 8" fill="none" stroke="#f4a261" stroke-width="3"/></svg></a>
      <a class="subject-tile" href="#">Business<svg width="14" height="22" viewBox="0 0 14 22"><path d="M3 3l8 8-8 8" fill="none" stroke="#f4a261" stroke-width="3"/></svg></a>
      <a class="subject-tile" href="#">Criminal Justice<svg width="14" height="22" viewBox="0 0 14 22"><path d="M3 3l8 8-8 8" fill="none" stroke="#f4a261" stroke-width="3"/></svg></a>
      <a class="subject-tile" href="#">Culinary Arts<svg width="14" height="22" viewBox="0 0 14 22"><path d="M3 3l8 8-8 8" fill="none" stroke="#f4a261" stroke-width="3"/></svg></a>
      <a class="subject-tile" href="#">Education &amp; Teaching<svg width="14" height="22" viewBox="0 0 14 22"><path d="M3 3l8 8-8 8" fill="none" stroke="#f4a261" stroke-width="3"/></svg></a>
      <a class="subject-tile" href="#">Engineering<svg width="14" height="22" viewBox="0 0 14 22"><path d="M3 3l8 8-8 8" fill="none" stroke="#f4a261" stroke-width="3"/></svg></a>
      <a class="subject-tile" href="#">Health Care<svg width="14" height="22" viewBox="0 0 14 22"><path d="M3 3l8 8-8 8" fill="none" stroke="#f4a261" stroke-width="3"/></svg></a>
      <a class="subject-tile" href="#">Human Services<svg width="14" height="22" viewBox="0 0 14 22"><path d="M3 3l8 8-8 8" fill="none" stroke="#f4a261" stroke-width="3"/></svg></a>
      <a class="subject-tile" href="#">Legal and Paralegal<svg width="14" height="22" viewBox="0 0 14 22"><path d="M3 3l8 8-8 8" fill="none" stroke="#f4a261" stroke-width="3"/></svg></a>
      <a class="subject-tile" href="#">Liberal Arts<svg width="14" height="22" viewBox="0 0 14 22"><path d="M3 3l8 8-8 8" fill="none" stroke="#f4a261" stroke-width="3"/></svg></a>
      <a class="subject-tile" href="#">Nursing<svg width="14" height="22" viewBox="0 0 14 22"><path d="M3 3l8 8-8 8" fill="none" stroke="#f4a261" stroke-width="3"/></svg></a>
      <a class="subject-tile" href="#">Political Science<svg width="14" height="22" viewBox="0 0 14 22"><path d="M3 3l8 8-8 8" fill="none" stroke="#f4a261" stroke-width="3"/></svg></a>
      <a class="subject-tile" href="#">Psychology<svg width="14" height="22" viewBox="0 0 14 22"><path d="M3 3l8 8-8 8" fill="none" stroke="#f4a261" stroke-width="3"/></svg></a>
      <a class="subject-tile" href="#">Religious Studies<svg width="14" height="22" viewBox="0 0 14 22"><path d="M3 3l8 8-8 8" fill="none" stroke="#f4a261" stroke-width="3"/></svg></a>
      <a class="subject-tile" href="#">Science &amp; Math<svg width="14" height="22" viewBox="0 0 14 22"><path d="M3 3l8 8-8 8" fill="none" stroke="#f4a261" stroke-width="3"/></svg></a>
      <a class="subject-tile last-left" href="#">Social Services<svg width="14" height="22" viewBox="0 0 14 22"><path d="M3 3l8 8-8 8" fill="none" stroke="#f4a261" stroke-width="3"/></svg></a>
      <a class="subject-tile last-right" href="#">Technology<svg width="14" height="22" viewBox="0 0 14 22"><path d="M3 3l8 8-8 8" fill="none" stroke="#f4a261" stroke-width="3"/></svg></a>
    </div>

    <nav class="footer-links">
      <a href="#">Home</a>
      <a href="#">Featured Schools</a>
      <a href="#">Degree By Level</a>
      <a href="#">Degree By Subject</a>
      <a href="#">Online Schools</a>
      <a href="#">Campus Schools</a>
      <a href="#">Site Map</a>
      <a href="#">About Us</a>
      <a href="#">Privacy Policy</a>
      <a href="#">Advertising</a>
      <a href="#">Unsubscribe</a>
    </nav>
  </section>
</div>
</body>
</html>
```